PowerPoint Design Project for specific credit card

We need a Presentation for a new product launch that this custom for attorneys. The purpose is for our team of sales agents to be able to meet with the law firms (attorneys or their office manager) and professionally show them what we can do for them.

Here's the "content"

Bramwell Ledger Services (LOGO) is pleased to Introduce QuillaPay!

Problem – CO-mingling funds! Never deposit retainer funds into your operating account!
Solution – The QuillaPay program is a custom card acceptance solution for attorneys, developed with the input of our bar association partners and their ethics committees. It is critical for attorneys to handle credit card transactions between their trust and operating accounts correctly. QuillaPay meets the requirements for the Continental Counsel Guild and most state trust account guidelines, as well as the Attorney’s Professional Code of Conduct.
QuillaPay not only separates your funds, it protects the attorney trust account from all 3rd party access. We restrict the ability of all other banking institutions from debiting monies from an attorney trust or IOLTA account.

Processing Options
Web-Based Virtual
The web-based virtual terminal option allows you to process credit card payments by logging into the QuillaPay system. Your secure login and password give you access to run payments, view deposits and reports. Processing through QuillaPay Web gives you the ability to process payments anywhere you have internet access.

Traditional Terminal
A traditional terminal system is a simple, easy to use option for attorneys that frequently meet clients in their office and handle payment immediately. Credit cards can either be swiped through the terminal or the card number can be typed in. Terminals do not require a separate phone line. Many attorneys split their terminal with an existing fax line.
QuillaPay Mobile
Your QuillaPay account can be used anywhere, anytime with the QuillaPay Mobile App. Mobile processing is available on all QuillaPay Web accounts and compatible with Zephon, Zepslate, and Koralux.
Benefits of Accepting Credit Cards
We’re a different kind of payment processor. We believe merchant accounts should be easy and we do our best to make the process of opening and maintaining a QuillaPay account as simple as possible. As our client you can look forward to personalized service and attention to detail that is not easily found. With a QuillaPay account you can:
Improve Cash Flow
Card acceptance is a powerful draw for new clients. The added convenience means you can accept payments in person, online, or as an added option on invoices.

Save Money
Through QuillaPay, members save up to 25% off processing fees. If you are currently accepting credit cards, we encourage you to compare your current processor.

Attract Clients
Payment by credit card is an increasingly popular payment option for attorneys. Accepting credit cards draws clients to your law practice and helps you win new business.

Save Time
A QuillaPay Merchant Account streamlines accounting and reduces the time your staff spends monitoring and managing your trust and operating accounts.

Frequently Asked Questions
What is a merchant account?
A merchant account gives a business the ability to take credit or debit cards in person, through the Internet, over the phone, by mail or even by fax.

How is a QuillaPay account different?
Unlike a standard merchant account, QuillaPay offers account options that are structured to handle the unique requirements of the attorney-client transaction. When your client pays by credit card, the funds are immediately separated into trust and operating accounts as required. All processing fees are deducted from your operating account keeping the balance of your trust account intact. You never have to worry about commingling client funds!

How much does a QuillaPay account cost?
Depending on how you want to accept client payments (in-person, over the phone, or through your website), there is a processing fee from Norda and TrueLink. In addition, you may have the expense of either a credit card machine or using a web-based “web-based terminal” to actually run your transactions. Many clients have their own system already and we are happy to accommodate. Lastly, there is a small monthly statement fee that covers account management and support. There is no contract, application, or start up fees and no monthly minimums. 888-614-2937

How quickly do I get paid?
From the date of the transaction, it usually takes 24 – 48 hours for the funds to deposit directly into your bank account.

What is the processing fee?
The processing fee or “Discount Rate” is the percentage that is deducted or “discounted” from the amount of the transaction. The Discount Rate covers the cost to move money electronically through the global processing network from the cardholder, their credit card company and finally as payment to you.

How are processing fees for the trust account paid?
All fees are deducted from the operating account. For example: if you accept a retainer by credit card, the dollar amount of the retainer is deposited into your appropriate trust account. The processing fee for that particular transaction is deducted at the end of the month from your operating account. Total processing fees for the month are deducted as a one-time debit from the operating account.

Can I pass the fees on to my client?
This is a common question amongst attorneys. Norda and TrueLink mandate that you cannot “penalize” a cardholder for using their card as a method of payment. Most attorneys consider the cost of credit card acceptance as a business expense, much like a phone line, long distance, etc. However, one option is to provide a “cash discount.” A cash discount means that you may charge a higher set fee, but discount your fee for clients that pay by check or cash. Overall, most of our clients see such an advantage with collections, billing and cash flow that the fees for processing credit cards are well worth the benefits!

What if I already accept credit cards: can you reprogram my credit card terminal?
We can reprogram the majority of terminal models over the phone. The process normally takes 10-15 minutes and you can begin accepting charges immediately with no down time.

Then create some kind of cool closing page!

Target Market(s)

law firms, attorneys

Industry/Entity Type

Credit Card

Requirements
Must have
• Must have both power point and PDF. I need to receive (if selected) the powerpoint in a non-locked out fashion so we can edit as needed.

Would like to see a nice presentation with lot's of graphics (very professional)

Would also like to have a one page flyer that corresponds to the presentation
Nice to have
• An actual "template" in case additional pages needed to be added later would be cool
Should not have
• Only boring script. I like pictures to explain it.

```html
<!DOCTYPE html>
<html lang="en">
<head>
<meta charset="utf-8">
<title>Web-Based Virtual</title>
<link rel="stylesheet" href="https://fonts.googleapis.com/css2?family=Jost:wght@400&family=Oswald:wght@600&display=swap">
<style>
  :root {
    --frame: #808080;
    --deep: #0b2d4f;
    --mid: #1d6a96;
    --light: #3a93be;
    --panel: rgba(8, 44, 92, 0.62);
    --panel-edge: rgba(235, 245, 255, 0.85);
    --ink: #ffffff;
    --navy: #0b2460;
    --green: #00a650;
  }
  * { box-sizing: border-box; margin: 0; padding: 0; }
  html, body { width: 1200px; height: 912px; overflow: hidden; background: var(--frame); }
  .slide {
    position: absolute; left: 24px; top: 24px; width: 1152px; height: 864px;
    overflow: hidden; background: var(--deep);
  }
  .backdrop {
    position: absolute; inset: 0;
    background:
      radial-gradient(ellipse 60% 55% at 48% 42%, var(--light) 0%, rgba(58,147,190,0) 70%),
      radial-gradient(ellipse 45% 60% at 15% 30%, #2c7fae 0%, rgba(44,127,174,0) 70%),
      linear-gradient(135deg, #145a86 0%, var(--mid) 40%, #17557e 70%, #08233f 100%);
  }
  .title-accent {
    position: absolute; left: 0; top: 30px; width: 8px; height: 66px; background: var(--ink);
  }
  .title {
    position: absolute; left: 22px; top: 26px;
    font-family: "Oswald", sans-serif; font-weight: 600; font-size: 50px; line-height: 72px;
    color: var(--ink); letter-spacing: 0.5px;
  }
  .point {
    position: absolute; background: var(--panel);
    border: 1.5px solid var(--panel-edge); border-radius: 5px;
    padding: 10px 18px;
    font-family: "Jost", sans-serif; font-size: 23px; line-height: 44px; color: var(--ink);
  }
  .point ul { list-style: none; }
  .point li::before { content: "\2022\00a0"; }
  .point .sub { padding-left: 58px; }
  .point-intro  { left: 86px;  top: 160px; width: 772px; height: 109px; }
  .point-access { left: 186px; top: 323px; width: 773px; height: 209px; }
  .point-reach  { left: 258px; top: 595px; width: 773px; height: 109px; }
  .footer-band { position: absolute; left: 0; bottom: 0; width: 100%; height: 34px; }
</style>
</head>
<body>
  <div class="slide">
    <div class="backdrop" role="img" aria-label="Blurred blue background of an online payment login screen"></div>
    <div class="title-accent"></div>
    <h1 class="title">Web-Based Virtual</h1>

    <div class="point point-intro">
      <ul><li>Enables processing credit card payments by logging into the QuillaPay system</li></ul>
    </div>

    <div class="point point-access">
      <ul>
        <li>Secure login gives access to</li>
        <li class="sub">Run payments</li>
        <li class="sub">View deposits</li>
        <li class="sub">View Reports</li>
      </ul>
    </div>

    <div class="point point-reach">
      <ul><li>Payments can be processed wherever internet access is available</li></ul>
    </div>

    <svg class="footer-band" viewBox="0 0 1152 34" preserveAspectRatio="none" aria-hidden="true">
      <rect x="0" y="7" width="1152" height="27" fill="var(--navy)"/>
      <polygon points="900,0 1152,0 1152,34 882,34" fill="var(--green)"/>
    </svg>
  </div>
</body>
</html>
```